依頼詳細
基本レイアウトについては
https://zuvaro.com/diagrams/7kq2m94T3XhpleWn
もしくは、添付データのワイヤーをご参照ください。

全体の雰囲気としては
http://www.morelid.co.jp/eco/forest/
のような和風・職人の雰囲気がありつつも、
あまり古臭くならないようなイメージを希望いたします。

色合いについては特に制限はないですが、上記を踏まえ
赤(エンジ)・オレンジ・紫・緑・ベージュなどが良いかと思います。

提出の写真素材があまり多くないのですが、
http://boxquiltry.jp/download/8fa27cd04b91e5a36d0c2bb7105e94f2d6a1c479
にアップロードしたものをご利用いただければ幸いです。

また、
http://vomre.jp/
などから、5000円程度までならこちらにて購入可能です。
カンプデータにて作成頂き、納品時に当方にて購入したデータに差し替えていただければと存じます。

【ロゴについて】
ロゴについては代表の家紋である
「剣片喰 (けんかたばみ)」を使用します。
添付データにjpgのデータを添付しております。
色合いについては、必ずしも黒である必要はないので、デザインに合わせて
ご調整いただいて結構です。

ページ数
1ページ
希望イメージ
シンプル 複雑
単色 カラフル
暗い 明るい
日常 高級
遊び心 厳粛
未来的 伝統的
女性的 男性的
希望する色
特に規定はないですが、和風をイメージを取り入れた色合いを希望します。
納品ファイル
• 高解像度JPG (.jpg)
• フォトショップ形式 (.psd)
補足説明
先方提出のイメージ写真については
下記URLからダウンロードしてご利用ください。

また、
http://vomre.jp/

【参考サイト】
hhttp://www.morelid.co.jp/eco/forest/
→全体の構成、誠実な印象とコンテンツの見やすさを気に入られています。
→色合いについては、必ずしもグリーンベースである必要はありません。

基本的には和風・職人の雰囲気を出すようなサイトが希望なのですが、
あまり和風すぎる、職人すぎる印象は出したくない要望がございます。
(代表自体が35歳と若いこと、マンションの緑地管理などを出していく希望があるため)

http://tokuvane.jp/
のような雰囲気だと、少し古臭すぎる印象がございます。

とはいえ
http://www.qrv-jp.com/
のような感じですと少しポップすぎる印象です

http://plinth-galore.com/2012/166.html
http://plinth-galore.com/2011/115.html
→フッター部分の参照
■ 選んだ理由

クライアントとの協議の結果、こちらの案を採用させて頂きました。
職人っぽい雰囲気でありつつ、今っぽい印象を残したデザインが
選考の決め手になりました。

■ 提案者全員のお礼・コメント

この度は多数ご提案いただきありがとうございました。
当選に至らなかったランサー様には大変心苦しいのですが、
次の機会がございましたら、是非ご提案頂ければ幸いです。
引続きよろしくお願いいたします。

```html
<!DOCTYPE html>
<html lang="ja">
<head>
<meta charset="utf-8">
<title>緑匠園 | 植木屋・造園・外構工事</title>
<link rel="stylesheet" href="https://fonts.googleapis.com/css2?family=Noto+Sans+JP:wght@400;700&family=Shippori+Mincho:wght@500;700&display=swap">
<style>
:root{
  --green:#4f7d2b;
  --green-dark:#3a5f1c;
  --green-light:#eef3e2;
  --cream:#f7f4ea;
  --brown:#a07c3f;
  --brown-light:#c9a867;
  --ink:#333;
  --muted:#777;
  --rule:#d8d2bf;
  --black:#111;
}
*{box-sizing:border-box;margin:0;padding:0}
html,body{width:1200px;height:2244px;overflow:hidden}
body{background:#fff;color:var(--ink);font-family:"Noto Sans JP",sans-serif;font-size:15px;line-height:1.6}
.mincho{font-family:"Shippori Mincho",serif}
ul{list-style:none}

/* header */
.site-header{height:120px;display:flex;align-items:center;justify-content:space-between;padding:0 56px}
.brand{display:flex;align-items:center;gap:14px}
.brand-mark{width:44px;height:44px;background:var(--black);border-radius:50%}
.brand-name{font-family:"Shippori Mincho",serif;font-weight:700;font-size:40px;color:var(--black);letter-spacing:4px}
.header-contact{display:flex;align-items:center;gap:20px}
.tel-block{text-align:right}
.tel-block .tel{font-family:"Shippori Mincho",serif;font-weight:700;font-size:28px;color:var(--black)}
.tel-block .addr{font-size:12px;color:var(--muted)}
.btn-estimate{display:block;background:linear-gradient(#c9a867,#a07c3f);color:#fff;font-weight:700;font-size:14px;line-height:1.5;padding:12px 22px;border-radius:4px;text-align:center}

/* nav */
.global-nav{height:34px;background:linear-gradient(var(--green),var(--green-dark))}
.global-nav ul{display:flex;height:100%;padding:0 56px}
.global-nav li{flex:1;color:#fff;font-size:15px;font-weight:700;display:flex;align-items:center;justify-content:center;border-right:1px solid rgba(255,255,255,.3)}
.global-nav li:last-child{border-right:0}

/* hero */
.hero{position:relative;height:450px;margin:0 56px;background:linear-gradient(160deg,#5b7a3a 0%,#7f9b52 40%,#3e5a24 100%)}
.hero-copy{position:absolute;left:40px;top:80px;font-family:"Shippori Mincho",serif;font-size:72px;color:#fff;writing-mode:vertical-rl;line-height:1.3}
.hero-lead{position:absolute;right:50px;top:50px;width:230px;height:230px;border-radius:50%;background:rgba(255,255,255,.85);display:flex;align-items:center;justify-content:center;font-family:"Shippori Mincho",serif;font-size:20px;color:var(--green-dark);writing-mode:vertical-rl;line-height:1.9}
.hero-thumbs{display:flex;gap:12px;margin:14px 56px 0}
.hero-thumbs div{flex:1;height:110px;background:linear-gradient(#6a8448,#3f5529)}

/* main */
.main{display:flex;gap:40px;padding:44px 56px 0}
.sidebar{width:176px;flex:none}
.content{flex:1}

.banner-mansion{height:192px;border:3px solid var(--green);background:linear-gradient(#fff,var(--green-light));padding:16px 12px;font-family:"Shippori Mincho",serif;font-weight:700;color:var(--green-dark);font-size:24px;line-height:1.35}
.banner-mansion span{display:inline-block;background:#f1e4a8;padding:0 4px;margin-bottom:6px}
.contact-box{margin-top:24px;border:3px solid var(--green);padding:12px 10px;text-align:center}
.contact-box h3{background:var(--green);color:#fff;font-size:16px;padding:4px 0}
.contact-box .tel{font-family:"Shippori Mincho",serif;font-weight:700;font-size:26px;color:var(--green-dark);margin:10px 0 12px;display:flex;align-items:center;justify-content:center;gap:4px}
.contact-box .mail{display:block;border:1px solid var(--brown);color:var(--brown);font-size:13px;font-weight:700;padding:8px 4px;border-radius:3px}
.side-nav{margin-top:80px;border-top:1px solid var(--rule)}
.side-nav li{padding:10px 6px 10px 18px;border-bottom:1px dotted var(--rule);font-size:14px;position:relative}
.side-nav li::before{content:"";position:absolute;left:4px;top:18px;border:5px solid transparent;border-left-color:var(--green)}

.section-title{font-family:"Shippori Mincho",serif;font-weight:700;font-size:22px;color:var(--ink);border-bottom:2px solid var(--green);padding-bottom:6px;margin-bottom:14px}
.news li{display:flex;gap:30px;padding:8px 0;border-bottom:1px dotted var(--rule);font-size:14px}
.news time{color:var(--green-dark);width:110px}

.intro{margin-top:40px;background:var(--cream);border:1px solid var(--rule);padding:22px;display:flex;gap:22px;height:368px}
.intro-text{flex:1}
.intro-text h2{font-family:"Shippori Mincho",serif;font-weight:700;font-size:20px;color:var(--green-dark);line-height:1.5;margin-bottom:16px;border-left:5px solid var(--green);padding-left:12px}
.intro-text p{font-size:14px;margin-bottom:12px}
.intro-text h3{font-size:16px;color:var(--brown);margin:10px 0 6px}
.intro-photo{width:300px;display:flex;flex-direction:column;gap:16px}
.intro-photo .ph{flex:1;background:linear-gradient(#8c7a55,#5c5133)}
.btn-more{display:block;background:linear-gradient(#c9a867,#a07c3f);color:#fff;font-weight:700;text-align:center;padding:10px;border-radius:4px}

.works{margin-top:36px}
.works ul{display:flex;gap:20px}
.works li{flex:1}
.works .ph{height:150px;background:linear-gradient(#7e9660,#485f2f)}
.works h4{font-size:14px;margin-top:8px}
.works p{font-size:12px;color:var(--muted);line-height:1.5}

/* footer */
.footer-scene{position:absolute;left:0;top:1760px;width:1200px;height:160px;background:linear-gradient(#fff 40%,#cfcfcf)}
.site-footer{position:absolute;left:0;top:1920px;width:1200px;height:324px;background:var(--black);color:#ddd;padding:28px 56px}
.site-footer .brand-mark{background:#fff}
.site-footer .brand-name{color:#fff}
.footer-inner{display:flex;gap:60px}
.footer-contact .tel{font-family:"Shippori Mincho",serif;font-weight:700;font-size:26px;color:#fff;margin-top:14px}
.footer-contact .addr{font-size:12px;color:#aaa}
.footer-contact .btn-estimate{margin-top:14px;width:220px}
.footer-links{display:grid;grid-template-columns:repeat(3,180px);gap:8px 20px;margin-top:70px;font-size:14px}
.footer-links li::before{content:"▶ ";color:var(--brown-light);font-size:10px}
.copyright{position:absolute;left:0;bottom:18px;width:100%;text-align:center;font-size:12px;color:#999}
</style>
</head>
<body>

<header class="site-header">
  <div class="brand"><span class="brand-mark"></span><span class="brand-name">緑匠園</span></div>
  <div class="header-contact">
    <div class="tel-block"><div class="tel">TEL 0120-318-462</div><div class="addr">神奈川県川崎市幸区南森町2-4-8</div></div>
    <a class="btn-estimate">お見積もり・<br>お問合せはこちら</a>
  </div>
</header>

<nav class="global-nav">
  <ul><li>トップページ</li><li>植木屋の仕事</li><li>造園・外構工事</li><li>マンション緑地管理</li><li>施工事例</li><li>よくある質問</li><li>会社案内</li></ul>
</nav>

<section class="hero" role="img" aria-label="緑豊かな日本庭園を座敷から眺めた写真">
  <p class="hero-copy">心を込めて</p>
  <p class="hero-lead">お客様のこころを、<br>お庭づくりに込めて</p>
</section>
<div class="hero-thumbs">
  <div role="img" aria-label="庭園の写真"></div>
  <div role="img" aria-label="和室から見る庭の写真"></div>
  <div role="img" aria-label="縁側の写真"></div>
  <div role="img" aria-label="植栽の写真"></div>
  <div role="img" aria-label="苔庭の写真"></div>
</div>

<div class="main">
  <aside class="sidebar">
    <div class="banner-mansion"><span>マンション</span><br>緑地管理<br>のご提案</div>
    <div class="contact-box">
      <h3>資料請求・お問い合せ</h3>
      <div class="tel">
        <svg width="20" height="20" viewBox="0 0 24 24"><path fill="currentColor" d="M6.6 10.8a15 15 0 006.6 6.6l2.2-2.2a1 1 0 011-.25 11.4 11.4 0 003.6.57 1 1 0 011 1V20a1 1 0 01-1 1A17 17 0 013 4a1 1 0 011-1h3.5a1 1 0 011 1c0 1.25.2 2.45.57 3.57a1 1 0 01-.25 1z"/></svg>
        0120-318-462
      </div>
      <a class="mail">メールでのお見積り<br>・お問合せはこちら</a>
    </div>
    <ul class="side-nav">
      <li>トップページ</li><li>植木屋の仕事について</li><li>造園・外構工事について</li><li>マンション緑地管理</li><li>施工事例</li><li>よくある質問</li><li>会社案内</li><li>お問い合せ</li>
    </ul>
  </aside>

  <div class="content">
    <section class="news">
      <h2 class="section-title">新着情報</h2>
      <ul>
        <li><time>2013年01月01日</time>新着情報のタイトルが入ります。新着情報のタイトル</li>
        <li><time>2013年01月01日</time>新着情報のタイトルが入ります。新着情報のタイトル</li>
        <li><time>2013年01月01日</time>新着情報のタイトルが入ります。新着情報のタイトル</li>
        <li><time>2013年01月01日</time>新着情報のタイトルが入ります。新着情報のタイトル</li>
        <li><time>2013年01月01日</time>新着情報のタイトルが入ります。新着情報のタイトル</li>
      </ul>
    </section>

    <section class="intro">
      <div class="intro-text">
        <h2>神奈川県川崎市幸区の植木屋・庭師・造園工事・外構工事は緑匠園にお任せ下さい！</h2>
        <p>お客様のお庭を心を込めて手入れいたします。植木の剪定から造園まで、丁寧な仕事をお約束します。</p>
        <p>マンションの緑地管理も承っております。管理会社様もお気軽にご相談ください。</p>
        <h3>● こんな仕事もできます</h3>
        <p>植木剪定、ブロック工事、フェンス工事、カーポート取り付けなど、外構工事も幅広く対応いたします。</p>
      </div>
      <div class="intro-photo">
        <div class="ph" role="img" aria-label="庭で作業する職人の写真"></div>
        <a class="btn-more">詳しくはこちら</a>
      </div>
    </section>

    <section class="works">
      <h2 class="section-title">施工事例</h2>
      <ul>
        <li><div class="ph" role="img" aria-label="植栽の施工事例写真"></div><h4>タイトル</h4><p>テキストテキストテキストテキスト</p></li>
        <li><div class="ph" role="img" aria-label="庭の小道の施工事例写真"></div><h4>タイトル</h4><p>テキストテキストテキストテキスト</p></li>
        <li><div class="ph" role="img" aria-label="竹垣の施工事例写真"></div><h4>タイトル</h4><p>テキストテキストテキストテキスト</p></li>
        <li><div class="ph" role="img" aria-label="庭園の施工事例写真"></div><h4>タイトル</h4><p>テキストテキストテキストテキスト</p></li>
      </ul>
    </section>
  </div>
</div>

<div class="footer-scene" role="img" aria-label="東屋と松の木のシルエットが並ぶ庭の風景"></div>

<footer class="site-footer">
  <div class="footer-inner">
    <div class="footer-contact">
      <div class="brand"><span class="brand-mark"></span><span class="brand-name">緑匠園</span></div>
      <div class="tel">TEL 0120-318-462</div>
      <div class="addr">神奈川県川崎市幸区南森町2-4-8</div>
      <a class="btn-estimate">お見積もり・お問合せはこちら</a>
    </div>
    <ul class="footer-links">
      <li>トップページ</li><li>マンション緑地管理</li><li>よくある質問</li>
      <li>植木屋の仕事について</li><li>施工事例</li><li>会社案内</li>
      <li>造園・外構工事について</li><li>サイトマップ</li><li>お問い合せ</li>
    </ul>
  </div>
  <p class="copyright">copyright © 2013 緑匠園 All Rights Reserved.</p>
</footer>

</body>
</html>
```